Stationary - Business Card/Letterhead and envelope design

Details for my new Stationery Design Project will be added soon. , I have two logos I am trying to decide on. I will upload the eps logos shortly. I have attached a file of what i have so far. I need urgently Business cards, but also will need a letterhead template and envelopes.

PLEASE NOTE THE DEADLINE SAYS 2 DAYS but I need business card design in LESS THAN A DAY.

thanks, Details for my new Stationery Design Project will be added soon. , I have two logos I am trying to decide on. I will upload the eps logos shortly. I have attached a file of what i have so far. I need urgently Business cards, but also will need a letterhead template and envelopes.

thanks
Updates

I have uploaded one of the logos you can work with. hopefully the other one comes soon.

details for the business card.

Marla Thorne

Managing Director

P&K Ventures Ltd

Bda: 1-441-555-0193

Email: marla@pkvnbda.com

web: www.pkvnbda.com

Industry/Entity Type

Business

```html
<!DOCTYPE html>
<html lang="en">
<head>
<meta charset="utf-8">
<title>P&amp;K Ventures Ltd — Stationery</title>
<link rel="stylesheet" href="https://fonts.googleapis.com/css2?family=Josefin+Slab:wght@400;600&family=Open+Sans:wght@400;600;700&display=swap">
<style>
  :root {
    --teal: #2ea3c0;
    --teal-soft: #5eb3c8;
    --brown: #7a6753;
    --paper: #ffffff;
    --backdrop: #e8e8e9;
    --ink: #3a3a3a;
    --window: #f2f2f2;
    --window-edge: #d9d9d9;
  }
  * { box-sizing: border-box; margin: 0; padding: 0; }
  html, body { width: 1200px; height: 900px; overflow: hidden; }
  body {
    position: relative;
    background: var(--backdrop);
    font-family: "Open Sans", Arial, sans-serif;
    color: var(--ink);
  }

  /* Brand name stands in for the mark */
  .brand-name {
    font-family: "Open Sans", Arial, sans-serif;
    font-weight: 600;
    color: var(--teal-soft);
    white-space: nowrap;
    letter-spacing: 0.2px;
  }

  /* Letterhead */
  .letterhead {
    position: absolute; left: 176px; top: 98px;
    width: 490px; height: 690px;
    background: var(--paper);
  }
  .header-rule { position: absolute; height: 2px; }
  .rule-teal { background: var(--teal); }
  .rule-brown { background: var(--brown); }
  .letterhead .rule-teal { left: 0; top: 42px; width: 26px; }
  .letterhead .brand-name { position: absolute; left: 30px; top: 28px; font-size: 15px; }
  .letterhead .rule-brown { left: 130px; top: 42px; width: 334px; }
  .header-url {
    position: absolute; font-size: 6px; color: var(--ink);
  }
  .letterhead .header-url { right: 26px; top: 33px; }

  .letter-body {
    position: absolute; left: 68px; top: 212px; width: 354px;
    font-family: "Josefin Slab", Georgia, serif;
    font-size: 10px; line-height: 12.3px; color: #444;
    text-align: justify; hyphens: auto;
  }
  .letter-body p { margin-bottom: 12.3px; }
  .letter-footer {
    position: absolute; left: 0; right: 0; top: 622px;
    text-align: center;
    font-family: "Josefin Slab", Georgia, serif;
    font-size: 9.5px; line-height: 12px; color: #333; font-weight: 600;
  }

  /* Business cards */
  .card {
    position: absolute; width: 200px; height: 127px; overflow: hidden;
    box-shadow: 0 2px 5px rgba(0,0,0,0.18);
  }
  .card-front { left: 745px; top: 98px; background: var(--brown); }
  .card-front .side-band {
    position: absolute; left: 0; top: 0; width: 75px; height: 100%;
    background: var(--teal);
  }
  .badge {
    position: absolute; border-radius: 50%; background: var(--paper);
    display: flex; align-items: center; justify-content: center;
  }
  .card-front .badge { left: 18px; top: 32px; width: 44px; height: 44px; }
  .card-front .badge .brand-name { font-size: 7px; }
  .card-name {
    position: absolute; left: 87px; top: 50px;
    color: #fff; font-size: 11px; line-height: 12px; letter-spacing: 0.2px;
  }
  .card-name strong { font-weight: 700; }
  .card-title {
    position: absolute; left: 87px; top: 62px;
    color: #fff; font-size: 7px;
  }
  .card-contacts {
    position: absolute; left: 87px; top: 92px; list-style: none;
    color: #fff; font-size: 5px; line-height: 7.5px;
  }
  .card-contacts li { display: flex; align-items: center; gap: 3px; }
  .card-contacts svg { width: 6px; height: 6px; }

  .card-back { left: 745px; top: 264px; background: var(--teal); }
  .card-back .badge { left: 56px; top: 19px; width: 88px; height: 88px; }
  .card-back .badge .brand-name { font-size: 12px; }
  .card-back .back-url {
    position: absolute; left: 0; right: 0; top: 112px;
    text-align: center; color: #fff; font-size: 5.5px;
  }

  /* Envelope */
  .envelope {
    position: absolute; left: 690px; top: 537px;
    width: 485px; height: 253px; background: var(--paper);
  }
  .envelope .rule-teal { left: 0; top: 38px; width: 30px; }
  .envelope .brand-name { position: absolute; left: 34px; top: 24px; font-size: 15px; }
  .envelope .rule-brown { left: 136px; top: 38px; width: 334px; }
  .envelope .header-url { right: 16px; top: 29px; }
  .address-window {
    position: absolute; left: 295px; top: 151px; width: 163px; height: 79px;
    border: 1px solid var(--window-edge); border-radius: 6px;
    background: var(--window);
  }
</style>
</head>
<body>

  <section class="letterhead" aria-label="Letterhead">
    <div class="header-rule rule-teal"></div>
    <div class="brand-name">P&amp;K Ventures</div>
    <div class="header-rule rule-brown"></div>
    <div class="header-url">www.pkvnbda.com</div>

    <div class="letter-body">
      <p>Lorem ipsum dolor sit amet,</p>
      <p>Lorem ipsum dolor sit amet, consectetur adipiscing elit. Donec orci purus, luctus vitae dignissim eu, iaculis sed purus. Vivamus faucibus, ipsum nec aliquet viverra, leo mauris condimentum ligula, sit amet sagittis enim ligula quis arcu. Nam egestas tortor id nisi porttitor mattis. In tortor ante, ultricies in suscipit a, tempus non massa. Vivamus et auctor mi. Fusce vel massa nulla. Phasellus nec eros mauris, et scelerisque orci. Donec malesuada orci vitae nulla accumsan porta a id massa. Quisque accumsan iaculis magna sit amet fringilla. Maecenas consequat, magna eget tincidunt semper, odio nibh rutrum mi, id feugiat ante nisi eu risus. Vestibulum nunc orci, rhoncus a placerat in, ultricies in mi. Cras mattis varius eros, vel fringilla nisi suscipit eget.</p>
      <p>Quisque scelerisque sagittis nulla at porttitor. Mauris a justo et tellus interdum tristique. Sed id augue vitae urna euismod commodo aliquet a quam. Pellentesque arcu velit, cursus et malesuada ut, consequat et diam. Nullam erat sem, rhoncus id ullamcorper vitae, rhoncus et arcu. In ultricies ultricies nulla, ut rutrum nisi iaculis at. Donec eu magna a metus ornare faucibus. Fusce aliquet faucibus ultricies. Morbi semper, est id tincidunt gravida, sem arcu adipiscing lacus, ac bibendum nulla leo eu purus. Quisque nec diam sed risus consectetur a ccumsan quis quis nibh. Vestibulum id purus lorem.</p>
      <p>Vivamus vehicula accumsan lacinia. Aliquam erat volutpat. Pellentesque consequat venenatis velit non gravida. Etiam et sem et nulla congue aliquam sed eget augue. Nulla facilisi. Pellentesque habitant morbi tristique senectus et netus et malesuada fames ac turpis egestas. Nulla a elit at sem iaculis congue. Nullam mollis tristique lobortis.</p>
    </div>

    <address class="letter-footer" style="font-style:normal">
      (912) 555-0147<br>
      yourname@pkvnmail.com<br>
      pkvnmail.com
    </address>
  </section>

  <section class="card card-front" aria-label="Business card front">
    <div class="side-band"></div>
    <div class="badge"><span class="brand-name">P&amp;K Ventures</span></div>
    <div class="card-name">MARLA <strong>THORNE</strong></div>
    <div class="card-title">Managing Director</div>
    <ul class="card-contacts">
      <li>
        <svg viewBox="0 0 6 6" aria-hidden="true"><rect x="0.3" y="0.3" width="5.4" height="5.4" fill="none" stroke="#fff" stroke-width="0.6"/><path d="M2 1.5 L2.7 1.5 L3 2.4 L2.6 2.8 Q3 3.6 3.5 3.9 L3.9 3.5 L4.6 3.8 L4.6 4.5 Q3.5 4.8 2.6 3.8 Q1.7 2.7 2 1.5 Z" fill="#fff"/></svg>
        1-441-555-0193
      </li>
      <li>
        <svg viewBox="0 0 6 6" aria-hidden="true"><rect x="0.3" y="0.3" width="5.4" height="5.4" fill="none" stroke="#fff" stroke-width="0.6"/><rect x="1.4" y="1.9" width="3.2" height="2.2" fill="none" stroke="#fff" stroke-width="0.5"/><path d="M1.4 1.9 L3 3.1 L4.6 1.9" fill="none" stroke="#fff" stroke-width="0.5"/></svg>
        marla@pkvnbda.com
      </li>
      <li>
        <svg viewBox="0 0 6 6" aria-hidden="true"><rect x="0.3" y="0.3" width="5.4" height="5.4" fill="none" stroke="#fff" stroke-width="0.6"/><circle cx="3" cy="3" r="1.6" fill="none" stroke="#fff" stroke-width="0.5"/><path d="M1.4 3 H4.6 M3 1.4 V4.6" stroke="#fff" stroke-width="0.4"/></svg>
        www.pkvnbda.com
      </li>
    </ul>
  </section>

  <section class="card card-back" aria-label="Business card back">
    <div class="badge"><span class="brand-name">P&amp;K Ventures</span></div>
    <div class="back-url">www.pkvnbda.com</div>
  </section>

  <section class="envelope" aria-label="Envelope">
    <div class="header-rule rule-teal"></div>
    <div class="brand-name">P&amp;K Ventures</div>
    <div class="header-rule rule-brown"></div>
    <div class="header-url">www.pkvnbda.com</div>
    <div class="address-window"></div>
  </section>

</body>
</html>
```